The Pixel Tavern Business card.

A Simple card with our Logo and contact information. To give to investors and other professionals.

We are a nerd themed bar.
our target market is young professionals age 21+ but the real purpose of this business card is to present to potential investors and other professionals with our contact information. as we are still looking for funding before we start up.

I am partial to green and my partner likes red we are open to iteration.

Target Market(s)

Investors

Industry/Entity Type

Business

Contact Information for Business Card

Marcus Henley (555) 730-6621 kent.w4100@mailbox-demo.net Brian Tolle (555) 918-2047 briant731@mailbox-demo.net

Font styles to use
Serif

Requirements
Nice to have
• Keep it simple but not boring.
• Use the Logos but feel free to edit them to match theme/colors.
• Keep the back clean and use one of the Logos.

```html
<!DOCTYPE html>
<html lang="en">
<head>
<meta charset="utf-8">
<title>The Pixel Tavern — Business Card</title>
<link rel="stylesheet" href="https://fonts.googleapis.com/css2?family=Arimo:wght@400;700&display=swap">
<style>
  :root {
    --page: #e8e5e0;
    --card-white: #ffffff;
    --card-black: #0c0c0c;
    --ink: #111111;
    --ink-soft: #555555;
    --brand-red: #e3122b;
    --brand-pink: #f6c4cb;
    --paper-white: #ffffff;
  }
  * { box-sizing: border-box; margin: 0; padding: 0; }
  html, body {
    width: 1200px;
    height: 950px;
    overflow: hidden;
  }
  body {
    background: var(--page);
    font-family: "Arimo", Arial, sans-serif;
    display: flex;
    flex-direction: column;
    align-items: center;
    justify-content: center;
    gap: 50px;
  }
  .card {
    position: relative;
    width: 720px;
    height: 411px;
    box-shadow: 0 10px 28px rgba(0,0,0,0.22);
    overflow: hidden;
  }

  /* Back */
  .card-back {
    background: var(--card-black);
    display: flex;
    align-items: center;
    justify-content: center;
  }
  .brand-name {
    font-weight: 700;
    text-transform: uppercase;
    letter-spacing: 0.04em;
    line-height: 1;
  }
  .card-back .brand-name {
    color: var(--paper-white);
    font-size: 44px;
  }

  /* Front */
  .card-front { background: var(--card-white); }
  .card-front .brand-name {
    position: absolute;
    left: 58px;
    top: 50%;
    transform: translateY(-50%) rotate(180deg);
    writing-mode: vertical-rl;
    color: var(--ink);
    font-size: 46px;
  }
  .progress-ring {
    position: absolute;
    left: 0;
    top: 0;
  }
  .contact {
    position: absolute;
    left: 470px;
    top: 205px;
    transform: translate(-50%, -50%);
    width: 230px;
    display: flex;
    flex-direction: column;
    gap: 7px;
  }
  .contact-name {
    font-weight: 700;
    font-size: 19px;
    color: var(--ink);
    margin-bottom: 4px;
  }
  .contact-line {
    display: flex;
    align-items: center;
    gap: 7px;
    font-size: 13.5px;
    color: var(--ink-soft);
    white-space: nowrap;
  }
  .contact-line svg { flex: none; }
</style>
</head>
<body>

  <section class="card card-back" aria-label="Card back">
    <span class="brand-name">The Pixel Tavern</span>
  </section>

  <section class="card card-front" aria-label="Card front">
    <span class="brand-name">The Pixel Tavern</span>

    <svg class="progress-ring" width="720" height="411" viewBox="0 0 720 411" aria-hidden="true">
      <defs>
        <linearGradient id="ringFade" x1="0.2" y1="0" x2="0.9" y2="1">
          <stop offset="0" stop-color="var(--brand-red)"/>
          <stop offset="0.55" stop-color="#ec5a6d"/>
          <stop offset="1" stop-color="var(--brand-pink)"/>
        </linearGradient>
      </defs>
      <path d="M 537.5 88.1 A 135 135 0 1 0 600.4 170.1"
            fill="none" stroke="url(#ringFade)" stroke-width="34"/>
    </svg>

    <div class="contact">
      <p class="contact-name">Marcus Henley</p>
      <p class="contact-line">
        <svg width="12" height="16" viewBox="0 0 12 16" aria-hidden="true">
          <rect x="1" y="1" width="10" height="14" rx="1.5" fill="none" stroke="#111" stroke-width="1.6"/>
          <rect x="4" y="12" width="4" height="1.4" fill="#111"/>
        </svg>
        (555) 730-6621
      </p>
      <p class="contact-line">
        <svg width="14" height="11" viewBox="0 0 14 11" aria-hidden="true">
          <rect x="0" y="0" width="14" height="11" fill="#111"/>
          <path d="M0 0 L7 6 L14 0" fill="none" stroke="#fff" stroke-width="1.3"/>
        </svg>
        kent.w4100@mailbox-demo.net
      </p>
    </div>
  </section>

</body>
</html>
```